New business card with our logo

we finalized our logo with the help of pixel harbor - now we need a business card using that logo. we are a metal service center providing raw steel and metal products for fabricating, contractors, artists, etc. we have the wording for the back of the card figured out (attached, no deviations from text please), just need help putting it all together.
would like the look of steel somehow incorporated in the design ... would like the black part of the logo to be steel or silver color (the S & BRANLEY)
Other font styles liked:
- calibri, arial, similar to those, modern looking
Colors
Designer to choose colors to be used in the design.
Requirements
Must have
- Back of card must haves are attached (no deviations from wording please).
- FRONT of card:
- logo
- address
- name
- office tel
- cell
- fax
- website
- address
Nice to have
- incorporate the look of steel or element of steel somehow
- names of the staff on front not in all caps, i.e. Rosvita not ROSVITA
- this industry is more industrial, not coffee or flower shop so design should be aligned with that
- design should be classic and tasteful

```html
<!DOCTYPE html>
<html lang="en">
<head>
<meta charset="utf-8">
<title>Branley Steel – Business Card</title>
<link rel="stylesheet" href="https://fonts.googleapis.com/css2?family=Open+Sans:wght@400;600&family=Roboto:wght@500;700&display=swap">
<style>
  :root {
    --backdrop: #e4e5e7;
    --charcoal: #39383a;
    --graphite: #424244;
    --steel: #a9abae;
    --blue: #0293d8;
    --blue-deep: #0077c2;
    --ink: #2b2b2d;
    --white: #ffffff;
  }
  * { margin: 0; padding: 0; box-sizing: border-box; }
  html, body { width: 1200px; height: 1200px; overflow: hidden; background: var(--backdrop); }
  body { position: relative; font-family: "Open Sans", sans-serif; color: var(--ink); }

  .card { position: absolute; overflow: hidden; box-shadow: 0 14px 28px rgba(0,0,0,.18); }

  /* Back of card */
  .card-back { left: 217px; top: 79px; width: 777px; height: 467px; background: var(--white); }
  .back-upper { position: absolute; left: 0; top: 0; width: 100%; height: 232px; background: var(--charcoal); }
  .back-lower { position: absolute; left: 0; top: 232px; width: 100%; height: 133px; background: var(--graphite); }
  .back-tab { position: absolute; left: 347px; top: 0; width: 83px; height: 101px; background: var(--blue); border-radius: 0 0 8px 8px; }
  .back-accent { position: absolute; left: 186px; top: 353px; width: 407px; height: 12px; background: var(--blue); }
  .brand-mark { position: absolute; left: 112px; top: 160px; }
  .brand-name {
    position: absolute; left: 176px; top: 168px; width: 262px; white-space: nowrap;
    font-family: "Roboto", sans-serif; font-weight: 700; font-size: 33px; letter-spacing: 0;
    color: var(--steel); line-height: 1;
  }
  .service-title {
    position: absolute; left: 456px; top: 173px;
    font-family: "Roboto", sans-serif; font-weight: 700; font-size: 20px; color: #d6d7d9; line-height: 1;
    white-space: nowrap;
  }
  .service-list {
    position: absolute; left: 456px; top: 197px;
    font-family: "Roboto", sans-serif; font-weight: 500; font-size: 13px; color: var(--blue); line-height: 1;
    display: flex; gap: 6px; align-items: center; white-space: nowrap;
  }
  .service-list .dot { width: 8px; height: 8px; border-radius: 50%; background: var(--blue); display: inline-block; }
  .product-line {
    position: absolute; left: 0; top: 391px; width: 100%; text-align: center;
    font-size: 15.5px; color: var(--ink); letter-spacing: .1px; padding-left: 12px; white-space: nowrap;
  }
  .delivery-bar {
    position: absolute; left: 185px; top: 431px; width: 407px; height: 36px; background: var(--graphite);
    color: var(--white); font-weight: 600; font-size: 12.5px; text-align: center; line-height: 36px; letter-spacing: -.2px;
  }

  /* Front of card */
  .card-front { left: 217px; top: 649px; width: 783px; height: 469px; background: var(--white); }
  .front-tab { position: absolute; left: 67px; top: 0; width: 84px; height: 162px; background: var(--blue-deep); border-radius: 0 0 8px 8px; }
  .front-mark { position: absolute; left: 168px; top: 108px; }
  .front-name {
    position: absolute; left: 222px; top: 108px;
    font-family: "Roboto", sans-serif; font-weight: 700; font-size: 24px; line-height: 23px; color: var(--ink);
  }
  .contact-list { position: absolute; left: 66px; top: 234px; list-style: none; }
  .contact-item { display: flex; align-items: center; margin-bottom: 10px; }
  .contact-item svg { width: 26px; height: 26px; flex: none; }
  .contact-text { margin-left: 23px; font-size: 16px; line-height: 21px; color: var(--ink); white-space: nowrap; }
  .front-accent { position: absolute; left: 430px; top: 98px; width: 12px; height: 278px; background: var(--blue-deep); }
  .person-panel { position: absolute; left: 442px; top: 0; width: 288px; height: 100%; background: var(--graphite); }
  .person-name { position: absolute; left: 45px; top: 92px; font-size: 26px; color: var(--white); white-space: nowrap; }
  .person-role { position: absolute; left: 45px; top: 128px; font-size: 16.5px; color: #e6e6e6; white-space: nowrap; }
</style>
</head>
<body>

<section class="card card-back">
  <div class="back-upper"></div>
  <div class="back-lower"></div>
  <div class="back-tab"></div>
  <svg class="brand-mark" width="54" height="54" viewBox="0 0 54 54" aria-hidden="true">
    <circle cx="27" cy="27" r="23" fill="none" stroke="var(--blue)" stroke-width="4"/>
  </svg>
  <div class="brand-name">BRANLEY STEEL</div>
  <div class="service-title">METAL SERVICE CENTRE</div>
  <div class="service-list">
    <span>CUT</span><span class="dot"></span><span>SHEAR</span><span class="dot"></span><span>PUNCH</span><span class="dot"></span><span>LIGHT FAB</span>
  </div>
  <div class="back-accent"></div>
  <p class="product-line">Structural Steel &nbsp;.&nbsp; Stainless &amp; Aluminum &nbsp;.&nbsp; Building Components &nbsp;.&nbsp; Rebar &nbsp;.&nbsp; Decking ... and more !</p>
  <div class="delivery-bar">Cut to size, Pick-up or Delivered !</div>
</section>

<section class="card card-front">
  <div class="front-tab"></div>
  <svg class="front-mark" width="44" height="44" viewBox="0 0 44 44" aria-hidden="true">
    <circle cx="22" cy="22" r="19" fill="none" stroke="var(--blue-deep)" stroke-width="3"/>
  </svg>
  <div class="front-name">BRANLEY<br>STEEL</div>

  <ul class="contact-list">
    <li class="contact-item">
      <svg viewBox="0 0 24 24" aria-hidden="true"><path fill="var(--blue-deep)" d="M3 8c0-2 2-3 9-3s9 1 9 3v2h-4V8.5c-1-.5-3-.7-5-.7s-4 .2-5 .7V10H3zM6 11l2-2h8l2 2v8H6zm6 2a2.5 2.5 0 100 5 2.5 2.5 0 000-5z"/></svg>
      <span class="contact-text">014 . 552 . 3190<br>014 . 552 . 3190</span>
    </li>
    <li class="contact-item">
      <svg viewBox="0 0 24 24" aria-hidden="true"><g fill="none" stroke="var(--blue-deep)" stroke-width="1.6"><circle cx="12" cy="12" r="9"/><ellipse cx="12" cy="12" rx="4" ry="9"/><path d="M3 12h18M4.5 7.5h15M4.5 16.5h15"/></g></svg>
      <span class="contact-text">info@branleysteel.com<br>www.branleysteel.com</span>
    </li>
    <li class="contact-item">
      <svg viewBox="0 0 24 24" aria-hidden="true"><path fill="#1f2f9a" d="M12 2a6.5 6.5 0 00-6.5 6.5C5.5 13.5 12 22 12 22s6.5-8.5 6.5-13.5A6.5 6.5 0 0012 2zm0 9a2.5 2.5 0 110-5 2.5 2.5 0 010 5z"/></svg>
      <span class="contact-text">1840 Harlow Avenue<br>Dunmore, AK 99702</span>
    </li>
  </ul>

  <div class="front-accent"></div>
  <div class="person-panel">
    <div class="person-name">Daren Okafor</div>
    <div class="person-role">Graphic Designer</div>
  </div>
</section>

</body>
</html>
```